Velnimo.org
Brackwater Residents association
plz star rating....
in the back of the card it should have the following
K&T BULKWARE SUPPLIERS
847 HAZELMOOR ROAD
OLVERTON MA. 02946
we will like the back ground of the card to be red... our colors are red yellow and blue.

```html
<!DOCTYPE html>
<html lang="en">
<head>
<meta charset="utf-8">
<title>Velnimo.org business card</title>
<link rel="stylesheet" href="https://fonts.googleapis.com/css2?family=Arimo:wght@400;700&display=swap">
<style>
  :root {
    --backdrop: #e9e6e1;
    --card-white: #ffffff;
    --brand-blue: #2b8fd6;
    --brand-yellow: #f2c418;
    --band-red: #c8202a;
    --band-red-light: #e2545a;
    --band-grey-dark: #9a9a9a;
    --band-grey-light: #f2f2f2;
    --ink-dark: #2a2a2a;
    --ink-white: #ffffff;
  }
  * { box-sizing: border-box; margin: 0; padding: 0; }
  html, body { width: 1200px; height: 408px; overflow: hidden; }
  body {
    background: var(--backdrop);
    font-family: "Arimo", Arial, sans-serif;
    position: relative;
  }
  .card {
    position: absolute;
    top: 42px;
    width: 530px;
    height: 324px;
    background: var(--card-white);
    overflow: hidden;
    box-shadow: 0 3px 10px rgba(0,0,0,0.25);
  }
  .card--front { left: 48px; }
  .card--back { left: 622px; }

  .brand {
    position: absolute;
    top: 26px;
    left: 0;
    width: 100%;
    text-align: center;
    color: var(--brand-blue);
  }
  .brand__name {
    display: inline-flex;
    align-items: center;
    gap: 10px;
    font-size: 44px;
    font-weight: 700;
    letter-spacing: -0.5px;
    line-height: 1;
  }
  .brand__mark {
    width: 22px;
    height: 22px;
    background: var(--brand-yellow);
  }
  .brand__tagline {
    margin-top: 8px;
    font-size: 17px;
    font-weight: 700;
    line-height: 1;
  }

  .name-band {
    position: absolute;
    top: 163px;
    left: 0;
    width: 100%;
    height: 42px;
    background: linear-gradient(to bottom, var(--band-grey-light) 0%, #ffffff 35%, #d6d6d6 75%, var(--band-grey-dark) 100%);
    display: flex;
    align-items: center;
    justify-content: center;
    color: var(--ink-dark);
    font-size: 16px;
  }
  .name-band__name { font-weight: 700; }
  .name-band__role { margin-left: 8px; }
  .name-band--slogan { font-weight: 700; font-size: 17px; }

  .contact-band {
    position: absolute;
    top: 205px;
    left: 0;
    width: 100%;
    height: 119px;
    background: linear-gradient(to bottom, var(--band-red-light) 0%, var(--band-red) 30%, var(--band-red) 100%);
    color: var(--ink-white);
    text-align: center;
    font-size: 12.5px;
    line-height: 1.3;
  }
  .contact-band__address { margin-top: 26px; }
  .contact-band__lines { margin-top: 14px; }
  .contact-band__web { margin-top: 4px; }

  .supplier { margin-top: 20px; }
  .supplier__name {
    font-weight: 700;
    font-size: 15px;
    letter-spacing: 0.5px;
    color: var(--brand-yellow);
  }
  .supplier__line { font-size: 12.5px; letter-spacing: 0.4px; }
  .contact-band__web--back { margin-top: 12px; }
</style>
</head>
<body>
  <section class="card card--front">
    <div class="brand">
      <div class="brand__name"><span class="brand__mark"></span>Velnimo.org</div>
      <div class="brand__tagline">Brackwater Residents Association</div>
    </div>
    <div class="name-band">
      <span class="name-band__name">Dorian Maltesca</span>
      <span class="name-band__role">/ President</span>
    </div>
    <div class="contact-band">
      <p class="contact-band__address">482 Quenby Street, Olverton, Ma 02946</p>
      <p class="contact-band__lines">P : 555-013-4471 &nbsp; F : 555-014-2290 &nbsp; E : velnimo2006@mailbox.com</p>
      <p class="contact-band__web">W: www.velnimo.com</p>
    </div>
  </section>

  <section class="card card--back">
    <div class="brand">
      <div class="brand__name"><span class="brand__mark"></span>Velnimo.org</div>
      <div class="brand__tagline">Brackwater Residents Association</div>
    </div>
    <div class="name-band name-band--slogan">we buy properties</div>
    <div class="contact-band">
      <div class="supplier">
        <p class="supplier__name">K&amp;T BULKWARE SUPPLIERS</p>
        <p class="supplier__line">847 HAZELMOOR ROAD</p>
        <p class="supplier__line">OLVERTON MA. 02946</p>
      </div>
      <p class="contact-band__web contact-band__web--back">www.velnimo.com</p>
    </div>
  </section>
</body>
</html>
```